Expense Tracker App for Young Adults

I need a mobile app designer to design an app UI for me. It is for an expense tracker app. I’ve attached a mind map of the various screens and features of the app.

I would like to see designs for this app which is targeted towards young adults (late teens & early 20s) just starting their career who want to plan their budgets and track their expenses.
Updates

Hello designers! I'm conscious that this is not a guaranteed project, so I can understand that some of you might be apprehensive. Just wanted to let you know that I'm willing to see your initial drafts that show your direction and theme for design. You don't have to design the whole app. In fact, it's better if you share your initial design ideas so that we can have a discussion and I can give my input. If I see some good initial designs, I will be happy to make this a guaranteed project. I'm simply being cautious since I'm bootstrapping this and funding out of my own pocket. Thank you for your understanding!

Target Market(s)

Young adults who are just starting their careers, late teens and early 20s.

Font styles to use
Sans Serif

Requirements
Must have
• Ease of use, smart and sleek, a guided setup wizard which will help users setup their account after signing up.
Should not have
• Clunky

```html
<!DOCTYPE html>
<html lang="en">
<head>
<meta charset="utf-8">
<title>Coinpath – App Design</title>
<link href="https://fonts.googleapis.com/css2?family=Poppins:wght@800&family=Source+Sans+3:wght@400;600;700&display=swap" rel="stylesheet">
<style>
:root{
  --canvas:#211f27;
  --brand:#9a3de0;
  --brand-soft:#c070e0;
  --brand-outline:#8b3fd6;
  --ink:#1b1720;
  --muted:#7c7684;
  --paper:#f7f7f9;
  --card:#ffffff;
  --phone-dark:#111013;
  --plum-1:#2b1633;
  --plum-2:#3d1d49;
  --plum-deep:#1c0f20;
  --red:#e53935;
  --cyan:#29b6e8;
  --yellow:#f4c430;
  --green:#4caf50;
  --violet:#a46be0;
  --nav-icon:#bfb3c6;
}
*{box-sizing:border-box;margin:0;padding:0}
html,body{width:1200px;height:960px;overflow:hidden;background:var(--canvas)}
body{font-family:"Source Sans 3",sans-serif;color:var(--ink)}
.stage{position:absolute;left:0;top:0;width:2156px;height:1725px;transform:scale(0.55659);transform-origin:0 0}
.abs{position:absolute}
.title{position:absolute;left:0;width:2156px;text-align:center;font-family:"Poppins",sans-serif;font-weight:800;line-height:1}
.title-main{top:100px;font-size:72px;color:var(--brand);letter-spacing:-1px}
.title-sub{top:186px;font-size:58px;color:transparent;-webkit-text-stroke:2px var(--brand-outline);letter-spacing:-1px}

.phone{position:absolute;top:353px;width:464px;height:1005px;overflow:hidden}
.phone-login{left:330px;background:#f6f5f7}
.phone-home{left:847px;background:var(--phone-dark)}
.phone-report{left:1363px;background:var(--phone-dark)}

.status-time{position:absolute;left:40px;top:17px;font-size:20px;font-weight:600;line-height:22px}
.status-icons{position:absolute;left:360px;top:20px;width:86px;height:16px}
.on-light{color:#2a2530}
.on-dark{color:#fff}

.t{position:absolute;line-height:1;white-space:nowrap}

/* login */
.brand-mark{position:absolute;left:0;width:464px;top:196px;text-align:center;font-size:24px;font-weight:600;color:var(--brand);line-height:1}
.brand-dot{display:inline-block;width:14px;height:14px;border-radius:50%;background:var(--brand);margin-right:8px;vertical-align:2px}
.login-panel{position:absolute;left:0;top:284px;width:464px;height:721px;border-radius:40px 40px 0 0;background:linear-gradient(180deg,var(--plum-1),#221027)}
.login-card{position:absolute;left:37px;top:384px;width:389px;height:290px;border-radius:30px;background:var(--card)}
.card-handle{position:absolute;left:163px;top:13px;width:62px;height:16px;border-radius:8px;background:#3a2a4a}
.field-line{position:absolute;left:74px;top:110px;width:291px;height:2px;background:#e3e0e6}
.field-text{font-size:16px;color:#77707d}
.pocket{position:absolute;left:0;top:587px;width:464px;height:418px}
.btn-login{position:absolute;left:121px;top:712px;width:222px;height:60px;border-radius:30px;background:linear-gradient(90deg,#8e3bd8,var(--brand-soft));color:#fff;font-weight:700;font-size:18px;text-align:center;line-height:60px;letter-spacing:.5px}
.link-forgot{position:absolute;left:0;width:478px;top:805px;text-align:center;font-size:17px;font-weight:600;color:#a64fe0;letter-spacing:.3px}
.signup-bar{position:absolute;left:37px;top:894px;width:388px;height:73px;border-radius:36px;background:var(--plum-deep)}
.signup-text{left:25px;top:27px;font-size:18px;color:#e7e2ea}
.btn-signup{position:absolute;left:275px;top:15px;width:97px;height:41px;border:2px solid #e7e2ea;border-radius:21px;color:#fff;font-size:15px;font-weight:700;text-align:center;line-height:37px}

/* home */
.avatar{position:absolute;left:19px;top:55px;width:52px;height:52px;border-radius:50%;background:linear-gradient(135deg,#2d6fd1,#e8a07a)}
.greet-small{left:91px;top:60px;font-size:13px;color:#cfc9d4;letter-spacing:.5px}
.greet-name{left:91px;top:77px;font-size:27px;font-weight:700;color:#fff}
.badge{position:absolute;left:370px;top:56px;width:22px;height:22px;border-radius:50%;background:var(--red);color:#fff;font-size:13px;font-weight:700;text-align:center;line-height:22px}
.sheet{position:absolute;left:12px;top:128px;width:440px;height:900px;border-radius:30px 30px 0 0;background:var(--paper)}
.balance-card{position:absolute;background:var(--card);border-radius:20px;box-shadow:0 6px 18px rgba(40,20,60,.08);overflow:hidden}
.label-caps{font-size:15px;color:#6f6877;letter-spacing:.3px}
.amount-big{font-size:33px;font-weight:700;color:var(--ink)}
.tab{font-size:18px;color:var(--ink)}
.tab-active{color:var(--brand)}
.tab-underline{position:absolute;left:165px;top:338px;width:86px;height:3px;border-radius:2px;background:var(--brand)}
.day-group{position:absolute;left:37px;width:389px;border-radius:16px;background:var(--card);box-shadow:0 4px 14px rgba(40,20,60,.05)}
.day-chip{position:absolute;left:0;top:20px;width:66px;height:42px;border-radius:0 12px 12px 0;background:#eeedf1;font-size:24px;font-weight:600;text-align:center;line-height:42px}
.day-caption{left:87px;top:26px;font-size:11px;color:#5c5662;letter-spacing:.3px}
.day-month{left:87px;top:43px;font-size:16px;color:#2c2731}
.day-total{right:18px;top:31px;font-size:21px;font-weight:700;color:var(--red)}
.dots{position:absolute;left:8px;width:373px;height:0;border-top:3px dotted #c9c5cd}
.txn-icon{position:absolute;width:48px;height:48px;border-radius:50%}
.txn-name{left:87px;font-size:19px;color:var(--ink)}
.txn-note{left:87px;font-size:13px;color:#7c7684}
.txn-amount{right:18px;font-size:18px;color:var(--red)}
.ic-cyan{background:linear-gradient(135deg,#45d6f0,#1f9ee0)}
.ic-yellow{background:linear-gradient(135deg,#ffd84a,#f0b020)}
.ic-green{background:linear-gradient(135deg,#5dcf62,#2e9a3c)}
.ic-violet{background:linear-gradient(135deg,#c08af0,#8e4fd8)}

/* nav */
.nav{position:absolute;left:0;top:919px;width:464px;height:86px}
.fab-ring{position:absolute;left:191px;top:880px;width:80px;height:80px;border-radius:50%;background:#fff;box-shadow:0 4px 10px rgba(0,0,0,.25)}
.fab{position:absolute;left:200px;top:889px;width:62px;height:62px;border-radius:50%;background:linear-gradient(135deg,#b866ea,#8a35d6)}
.home-bar{position:absolute;left:149px;top:987px;width:166px;height:6px;border-radius:3px;background:#fff}

/* report */
.report-small{left:20px;top:60px;font-size:14px;color:#d7d2db;letter-spacing:.5px}
.report-range{left:20px;top:78px;font-size:23px;font-weight:700;color:#fff}
.seg-btn{position:absolute;top:133px;width:200px;height:49px;border-radius:8px;color:#fff;font-size:14px;font-weight:600;line-height:49px;padding-left:55px}
.seg-active{left:24px;background:#9b4ee0}
.seg-idle{left:238px;background:#2e2e33}
.balance-col{position:absolute;top:30px;width:200px;text-align:center;line-height:1}
.balance-col .label-caps{font-size:13px}
.balance-col .amount{margin-top:10px;font-size:25px;font-weight:700}
.divider{position:absolute;left:206px;top:28px;width:2px;height:46px;background:#d9d5dd}
.sect-title{left:37px;top:354px;font-size:22px;font-weight:600;color:var(--ink)}
.sect-amount{right:38px;top:354px;font-size:22px;font-weight:700;color:var(--red)}
.pct{font-size:13px;color:#2c2731}
.cat-heading{left:37px;top:646px;font-size:13px;font-weight:600;color:#2c2731;letter-spacing:.3px}
.cat-card{position:absolute;width:187px;height:92px;border-radius:12px;background:var(--card);box-shadow:0 4px 14px rgba(40,20,60,.06)}
.cat-card .txn-icon{left:12px;top:12px;width:38px;height:38px}
.cat-amount{right:12px;top:19px;font-size:20px;font-weight:600;color:var(--red)}
.cat-label{left:14px;top:62px;font-size:16px;color:var(--ink)}
</style>
</head>
<body>
<svg width="0" height="0" style="position:absolute">
  <defs>
    <symbol id="i-cup" viewBox="0 0 24 24"><path d="M5 9h11v6a4 4 0 0 1-4 4H9a4 4 0 0 1-4-4z M16 11h2a2 2 0 0 1 0 4h-2 M8 4v3 M11 4v3 M14 4v3" fill="none" stroke="currentColor" stroke-width="1.8" stroke-linecap="round" stroke-linejoin="round"/></symbol>
    <symbol id="i-bill" viewBox="0 0 24 24"><path d="M6 3h10v18H6z M9 7h4 M9 11h4 M9 15h2 M16 13h3v6a2 2 0 0 1-2 2" fill="none" stroke="currentColor" stroke-width="1.8" stroke-linejoin="round" stroke-linecap="round"/></symbol>
    <symbol id="i-bag" viewBox="0 0 24 24"><path d="M5 7h14l-1 13H6z M9 10a3 3 0 0 0 6 0" fill="none" stroke="currentColor" stroke-width="1.8" stroke-linejoin="round" stroke-linecap="round"/></symbol>
    <symbol id="i-wallet" viewBox="0 0 24 24"><path d="M4 8h14a2 2 0 0 1 2 2v8a2 2 0 0 1-2 2H6a2 2 0 0 1-2-2z M4 8l10-4 2 4 M15 12h5v4h-5z" fill="none" stroke="currentColor" stroke-width="1.8" stroke-linejoin="round"/></symbol>
    <symbol id="i-pie" viewBox="0 0 24 24"><path d="M12 4a8 8 0 1 0 8 8h-8z M14 2a8 8 0 0 1 8 8h-8z" fill="none" stroke="currentColor" stroke-width="1.8" stroke-linejoin="round"/></symbol>
    <symbol id="i-target" viewBox="0 0 24 24"><circle cx="12" cy="12" r="9" fill="none" stroke="currentColor" stroke-width="1.8"/><circle cx="12" cy="12" r="5" fill="none" stroke="currentColor" stroke-width="1.8"/><circle cx="12" cy="12" r="1.6" fill="currentColor"/></symbol>
    <symbol id="i-grid" viewBox="0 0 24 24"><path d="M3 3h7v7H3z M14 3h7v7h-7z M3 14h7v7H3z M14 14h7v7h-7z" fill="none" stroke="currentColor" stroke-width="1.8"/></symbol>
    <symbol id="i-bell" viewBox="0 0 24 24"><path d="M6 17V11a6 6 0 0 1 12 0v6l2 2H4z M10 21h4" fill="none" stroke="currentColor" stroke-width="1.8" stroke-linejoin="round" stroke-linecap="round"/></symbol>
    <symbol id="i-filter" viewBox="0 0 24 24"><path d="M3 4h18l-7 8v7l-4 2v-9z" fill="none" stroke="currentColor" stroke-width="1.8" stroke-linejoin="round"/></symbol>
    <symbol id="i-calendar" viewBox="0 0 24 24"><path d="M4 6h16v14H4z M4 10h16 M8 3v5 M16 3v5" fill="none" stroke="currentColor" stroke-width="1.8" stroke-linecap="round"/><path d="M8 13h1M12 13h1M16 13h1M8 16h1M12 16h1M16 16h1" stroke="currentColor" stroke-width="1.8" stroke-linecap="round"/></symbol>
    <symbol id="i-user" viewBox="0 0 24 24"><circle cx="12" cy="8" r="4" fill="none" stroke="currentColor" stroke-width="1.8"/><path d="M4 21a8 8 0 0 1 16 0z" fill="none" stroke="currentColor" stroke-width="1.8" stroke-linejoin="round"/></symbol>
    <symbol id="i-lock" viewBox="0 0 24 24"><path d="M5 11h14v10H5z M8 11V7a4 4 0 0 1 8 0v4" fill="none" stroke="currentColor" stroke-width="1.8" stroke-linejoin="round"/></symbol>
    <symbol id="i-history" viewBox="0 0 24 24"><path d="M4 12a8 8 0 1 1 2.3 5.6 M4 6v6h6" fill="none" stroke="currentColor" stroke-width="1.8" stroke-linecap="round" stroke-linejoin="round"/><text x="12" y="16" font-size="10" font-weight="700" text-anchor="middle" fill="currentColor" font-family="sans-serif">$</text></symbol>
    <symbol id="i-goal" viewBox="0 0 24 24"><path d="M12 3a9 9 0 1 0 9 9 M8 12l3 3 8-9" fill="none" stroke="currentColor" stroke-width="1.8" stroke-linecap="round" stroke-linejoin="round"/></symbol>
    <symbol id="i-status" viewBox="0 0 86 16"><rect x="0" y="10" width="3" height="5" rx="1" fill="currentColor"/><rect x="5" y="7" width="3" height="8" rx="1" fill="currentColor"/><rect x="10" y="4" width="3" height="11" rx="1" fill="currentColor"/><rect x="15" y="1" width="3" height="14" rx="1" fill="currentColor"/><path d="M28 6a11 11 0 0 1 16 0 M31 9a7 7 0 0 1 10 0" fill="none" stroke="currentColor" stroke-width="2.2" stroke-linecap="round"/><circle cx="36" cy="13" r="2" fill="currentColor"/><rect x="52" y="2" width="28" height="12" rx="3" fill="none" stroke="currentColor" stroke-width="1.4"/><rect x="54" y="4" width="24" height="8" rx="2" fill="currentColor"/><rect x="82" y="6" width="2" height="4" rx="1" fill="currentColor"/></symbol>
    <linearGradient id="g-nav" x1="0" y1="0" x2="0" y2="1"><stop offset="0" stop-color="#4a2158"/><stop offset="1" stop-color="#1f0e26"/></linearGradient>
    <linearGradient id="g-pocket" x1="0" y1="0" x2="0" y2="1"><stop offset="0" stop-color="#44214f"/><stop offset="1" stop-color="#24112b"/></linearGradient>
  </defs>
</svg>

<main class="stage">
  <h1 class="title title-main">Expense Tracker</h1>
  <h2 class="title title-sub">App Design</h2>

  <!-- Login screen -->
  <section class="phone phone-login">
    <span class="status-time on-light">9:41</span>
    <svg class="status-icons on-light"><use href="#i-status"/></svg>
    <div class="brand-mark"><span class="brand-dot"></span>Coinpath</div>

    <div class="login-panel"></div>
    <span class="t" style="left:37px;top:324px;font-size:32px;font-weight:700;color:#fff">Log in</span>

    <div class="login-card">
      <div class="card-handle"></div>
      <svg class="abs" style="left:26px;top:69px;width:24px;height:24px;color:#3a2a4a"><use href="#i-user"/></svg>
      <span class="t field-text" style="left:74px;top:73px">username or email</span>
      <div class="field-line"></div>
      <svg class="abs" style="left:26px;top:131px;width:24px;height:24px;color:#3a2a4a"><use href="#i-lock"/></svg>
      <span class="t field-text" style="left:74px;top:135px">password</span>
    </div>

    <svg class="pocket" viewBox="0 0 464 418">
      <path d="M0,40 Q0,0 40,0 L181,0 A50,50 0 0 0 281,0 L424,0 Q464,0 464,40 L464,418 L0,418 Z" fill="url(#g-pocket)"/>
      <path d="M12,366 L12,52 Q12,12 52,12 L168,12 A64,64 0 0 0 294,12 L412,12 Q452,12 452,52 L452,366 Q452,406 412,406 L52,406 Q12,406 12,366 Z" fill="none" stroke="#9a8ca3" stroke-width="2" stroke-dasharray="14 9"/>
    </svg>

    <div class="btn-login">LOG IN</div>
    <div class="link-forgot">FORGOT PASSWORD?</div>
    <div class="signup-bar">
      <span class="t signup-text">Don’t have an account?</span>
      <div class="btn-signup">SIGN UP</div>
    </div>
  </section>

  <!-- Home screen -->
  <section class="phone phone-home">
    <span class="status-time on-dark">9:41</span>
    <svg class="status-icons on-dark"><use href="#i-status"/></svg>
    <div class="avatar" role="img" aria-label="User profile photo"></div>
    <span class="t greet-small">GOOD MORNING</span>
    <span class="t greet-name">Marlo</span>
    <svg class="abs" style="left:355px;top:67px;width:30px;height:30px;color:#fff"><use href="#i-bell"/></svg>
    <div class="badge">8</div>
    <svg class="abs" style="left:409px;top:67px;width:30px;height:30px;color:#fff"><use href="#i-filter"/></svg>

    <div class="sheet"></div>
    <div class="balance-card" style="left:25px;top:139px;width:414px;height:136px">
      <svg class="abs" style="left:290px;top:-42px;width:160px;height:170px">
        <circle cx="88" cy="80" r="80" fill="#f0e0f8"/>
        <circle cx="88" cy="80" r="60" fill="#d7a8ee"/>
        <circle cx="88" cy="80" r="42" fill="#a04ee0"/>
        <path d="M72 72 q8 -8 16 0 q8 10 0 22 q-8 6 -16 0 q-8 -12 0 -22z" fill="#fff"/>
        <text x="80" y="93" font-size="14" font-weight="700" fill="#a04ee0" text-anchor="middle" font-family="sans-serif">$</text>
        <path d="M94 78h14M94 85h14M94 92h14" stroke="#fff" stroke-width="3" stroke-linecap="round"/>
      </svg>
      <span class="t label-caps" style="left:25px;top:31px">CURRENT BALANCE</span>
      <span class="t amount-big" style="left:25px;top:62px">$1,450.00</span>
    </div>

    <span class="t tab" style="left:37px;top:307px">Last Month</span>
    <span class="t tab tab-active" style="left:163px;top:307px">This Month</span>
    <span class="t tab" style="left:290px;top:307px">Future</span>
    <div class="tab-underline"></div>

    <div class="day-group" style="top:360px;height:262px">
      <div class="day-chip">18</div>
      <span class="t day-caption">TODAY</span>
      <span class="t day-month">September 2020</span>
      <span class="t day-total">-120.00</span>
      <div class="dots" style="top:83px"></div>
      <div class="txn-icon ic-cyan" style="left:19px;top:114px"><svg class="abs" style="left:11px;top:11px;width:26px;height:26px;color:#fff"><use href="#i-cup"/></svg></div>
      <span class="t txn-name" style="top:118px">Café</span>
      <span class="t txn-note" style="top:143px">Large coffee &amp; 1 sliced cake</span>
      <span class="t txn-amount" style="top:129px">-20.00</span>
      <div class="txn-icon ic-yellow" style="left:19px;top:188px"><svg class="abs" style="left:11px;top:11px;width:26px;height:26px;color:#fff"><use href="#i-bill"/></svg></div>
      <span class="t txn-name" style="top:192px">Bills</span>
      <span class="t txn-note" style="top:217px">Internet</span>
      <span class="t txn-amount" style="top:203px">-100.00</span>
    </div>

    <div class="day-group" style="top:641px;height:187px">
      <div class="day-chip">17</div>
      <span class="t day-caption">YESTERDAY</span>
      <span class="t day-month">September 2020</span>
      <span class="t day-total">-250.00</span>
      <div class="dots" style="top:83px"></div>
      <div class="txn-icon ic-green" style="left:19px;top:114px"><svg class="abs" style="left:11px;top:11px;width:26px;height:26px;color:#fff"><use href="#i-bag"/></svg></div>
      <span class="t txn-name" style="top:118px">Shopping</span>
      <span class="t txn-note" style="top:143px">1 pair of shoes</span>
      <span class="t txn-amount" style="top:129px">-250.00</span>
    </div>

    <div class="day-group" style="top:847px;height:160px">
      <div class="day-chip">16</div>
      <span class="t day-caption">WEDNESDAY</span>
      <span class="t day-month">September 2020</span>
      <span class="t day-total">-80.00</span>
    </div>

    <svg class="nav" viewBox="0 0 464 86">
      <path d="M0,30 Q0,0 30,0 L178,0 A54,54 0 0 0 284,0 L434,0 Q464,0 464,30 L464,86 L0,86 Z" fill="url(#g-nav)"/>
      <rect x="31" y="6" width="32" height="3" rx="1.5" fill="#fff"/>
      <use href="#i-wallet" x="33" y="19" width="28" height="28" color="#fff"/>
      <use href="#i-pie" x="126" y="19" width="28" height="28" color="#bfb3c6"/>
      <use href="#i-target" x="311" y="19" width="28" height="28" color="#bfb3c6"/>
      <use href="#i-grid" x="404" y="19" width="28" height="28" color="#bfb3c6"/>
    </svg>
    <div class="fab-ring"></div>
    <div class="fab"><svg class="abs" style="left:0;top:0;width:62px;height:62px"><path d="M31 20v18M22 29h18" stroke="#fff" stroke-width="3" stroke-linecap="round"/><path d="M22 45q9 5 18 0" fill="none" stroke="#fff" stroke-width="2" stroke-linecap="round"/></svg></div>
    <div class="home-bar"></div>
  </section>

  <!-- Report screen -->
  <section class="phone phone-report">
    <span class="status-time on-dark">9:41</span>
    <svg class="status-icons on-dark"><use href="#i-status"/></svg>
    <span class="t report-small">VIEW REPORT</span>
    <span class="t report-range">1 Sep 2020 - 18 Sep 2020</span>
    <svg class="abs" style="left:408px;top:66px;width:32px;height:32px;color:#fff"><use href="#i-calendar"/></svg>

    <div class="seg-btn seg-active"><svg class="abs" style="left:12px;top:10px;width:30px;height:30px;color:#fff"><use href="#i-history"/></svg>Historical Expenses</div>
    <div class="seg-btn seg-idle"><svg class="abs" style="left:12px;top:10px;width:30px;height:30px;color:#fff"><use href="#i-goal"/></svg>Progress Against Goals</div>

    <div class="sheet" style="top:207px;width:439px"></div>
    <div class="balance-card" style="left:25px;top:219px;width:413px;height:98px">
      <div class="balance-col" style="left:-3px"><div class="label-caps">CURRENT BALANCE</div><div class="amount">$2,580.00</div></div>
      <div class="divider"></div>
      <div class="balance-col" style="left:217px"><div class="label-caps">ENDING BALANCE</div><div class="amount">$1,450.00</div></div>
    </div>

    <span class="t sect-title">Expenses</span>
    <span class="t sect-amount">$1,130.00</span>

    <svg class="abs" style="left:0;top:380px;width:464px;height:240px" viewBox="0 0 464 240">
      <path d="M246 55V90 M104 148H172 M292 165H355" stroke="#444" stroke-width="1.5"/>
      <circle cx="231" cy="150" r="50" fill="none" stroke="#29b6e8" stroke-width="24"/>
      <circle cx="231" cy="150" r="50" fill="none" stroke="#4caf50" stroke-width="24" stroke-dasharray="179.1 314.16" transform="rotate(-90 231 150)"/>
      <circle cx="231" cy="150" r="50" fill="none" stroke="#f4c430" stroke-width="24" stroke-dasharray="15.7 314.16" transform="rotate(-90 231 150)"/>
      <circle cx="246" cy="55" r="15" fill="#f4c430"/>
      <use href="#i-bill" x="237" y="46" width="18" height="18" color="#fff"/>
      <circle cx="104" cy="148" r="15" fill="#29b6e8"/>
      <use href="#i-cup" x="95" y="139" width="18" height="18" color="#fff"/>
      <circle cx="355" cy="165" r="15" fill="#4caf50"/>
      <use href="#i-bag" x="346" y="156" width="18" height="18" color="#fff"/>
    </svg>
    <span class="t pct" style="left:236px;top:400px">5%</span>
    <span class="t pct" style="left:50px;top:522px">43%</span>
    <span class="t pct" style="left:383px;top:539px">52%</span>

    <span class="t cat-heading">CATEGORIES (TAP TO VIEW MORE DETAILS)</span>
    <div class="cat-card" style="left:37px;top:675px">
      <div class="txn-icon ic-green"><svg class="abs" style="left:8px;top:8px;width:22px;height:22px;color:#fff"><use href="#i-bag"/></svg></div>
      <span class="t cat-amount">$587.60</span><span class="t cat-label">Shopping</span>
    </div>
    <div class="cat-card" style="left:239px;top:675px">
      <div class="txn-icon ic-cyan"><svg class="abs" style="left:8px;top:8px;width:22px;height:22px;color:#fff"><use href="#i-cup"/></svg></div>
      <span class="t cat-amount">$485.90</span><span class="t cat-label">Foods</span>
    </div>
    <div class="cat-card" style="left:37px;top:780px">
      <div class="txn-icon ic-yellow"><svg class="abs" style="left:8px;top:8px;width:22px;height:22px;color:#fff"><use href="#i-bill"/></svg></div>
      <span class="t cat-amount">$56.50</span><span class="t cat-label">Bills &amp; Utilities</span>
    </div>
    <div class="cat-card" style="left:239px;top:780px">
      <div class="txn-icon ic-violet"><svg class="abs" style="left:8px;top:8px;width:22px;height:22px;color:#fff"><use href="#i-wallet"/></svg></div>
      <span class="t cat-amount">$0.00</span><span class="t cat-label">Others</span>
    </div>

    <svg class="nav" viewBox="0 0 464 86">
      <path d="M0,30 Q0,0 30,0 L178,0 A54,54 0 0 0 284,0 L434,0 Q464,0 464,30 L464,86 L0,86 Z" fill="url(#g-nav)"/>
      <rect x="124" y="6" width="32" height="3" rx="1.5" fill="#fff"/>
      <use href="#i-wallet" x="33" y="19" width="28" height="28" color="#bfb3c6"/>
      <use href="#i-pie" x="126" y="19" width="28" height="28" color="#fff"/>
      <use href="#i-target" x="311" y="19" width="28" height="28" color="#bfb3c6"/>
      <use href="#i-grid" x="404" y="19" width="28" height="28" color="#bfb3c6"/>
    </svg>
    <div class="fab-ring"></div>
    <div class="fab"><svg class="abs" style="left:0;top:0;width:62px;height:62px"><path d="M31 20v18M22 29h18" stroke="#fff" stroke-width="3" stroke-linecap="round"/><path d="M22 45q9 5 18 0" fill="none" stroke="#fff" stroke-width="2" stroke-linecap="round"/></svg></div>
    <div class="home-bar"></div>
  </section>
</main>
</body>
</html>
```